Business Card for Makeup Artist

I need a business card designed for my makeup and hair artistry business which is primarily events and weddings focused. The card needs to be sleek, simple, stylish and appealing to women. I would prefer a white background but open to suggestions also. I also love the marble background look. I have attached some example pics. It needs to be a double sided card with logo and/or design on one side and contact details in the centre of the card on the other side. NO LOGO ON BACK. Examples attached.

Target Market(s)

Females age 14-55

Industry/Entity Type

Business

Contact Information for Business Card

Nora Vint
Principal Makeup Artist
P: 0413 925 214
E: nora@lumirabeauty.com.au
W: www.lumirabeauty.com.au

Requirements
Should not have
• No yellow, green, red or blue in the design.

```html
<!DOCTYPE html>
<html lang="en">
<head>
<meta charset="utf-8">
<title>Lumira Makeup Artistry — Business Card</title>
<link rel="stylesheet" href="https://fonts.googleapis.com/css2?family=Roboto:wght@300;400;500&display=swap">
<style>
  :root {
    --canvas-bg: #e9e6e3;
    --card-white: #ffffff;
    --card-black: #050505;
    --ink-grey: #5c5c5c;
    --ink-dark: #333333;
    --accent-pink: #ec5fc8;
    --rule-grey: #4a4a4a;
    --shadow: rgba(0, 0, 0, 0.18);
  }
  * { box-sizing: border-box; margin: 0; padding: 0; }
  html, body {
    width: 1200px;
    height: 892px;
    overflow: hidden;
  }
  body {
    background: var(--canvas-bg);
    font-family: "Roboto", Arial, sans-serif;
    display: flex;
    flex-direction: column;
    align-items: center;
    justify-content: center;
    gap: 60px;
  }
  .card {
    position: relative;
    width: 600px;
    height: 343px;
    box-shadow: 0 10px 28px var(--shadow);
    overflow: hidden;
  }
  .card__band {
    position: absolute;
    left: 0;
    right: 0;
    bottom: 0;
    height: 22px;
    background: var(--accent-pink);
  }
  .card__rule {
    position: absolute;
    left: 0;
    right: 0;
    bottom: 28px;
    height: 3px;
  }

  /* Contact side: details only, centred */
  .card--contact { background: var(--card-white); }
  .card--contact .card__rule { background: var(--rule-grey); }
  .details {
    position: absolute;
    left: 0;
    right: 0;
    top: 0;
    bottom: 31px;
    display: flex;
    flex-direction: column;
    align-items: center;
    justify-content: center;
    text-align: center;
  }
  .details__name {
    font-weight: 400;
    font-size: 32px;
    line-height: 1.1;
    color: var(--accent-pink);
  }
  .details__title {
    font-weight: 500;
    font-size: 17px;
    line-height: 1.3;
    color: var(--ink-dark);
  }
  .details__divider {
    width: 220px;
    height: 1.5px;
    margin: 16px 0 18px;
    background: var(--rule-grey);
  }
  .contact {
    list-style: none;
    font-weight: 400;
    font-size: 14px;
    color: var(--ink-dark);
    text-align: left;
  }
  .contact__item {
    display: flex;
    align-items: center;
    gap: 10px;
    margin-bottom: 9px;
  }
  .contact__item:last-child { margin-bottom: 0; }
  .contact__icon {
    width: 14px;
    height: 14px;
    flex: none;
  }

  /* Brand side */
  .card--brand { background: var(--card-black); }
  .card--brand .card__rule { background: var(--card-white); height: 2px; }
  .brand {
    position: absolute;
    left: 0;
    width: 100%;
    top: 92px;
    text-align: center;
  }
  .brand__name {
    font-weight: 300;
    font-size: 92px;
    line-height: 1;
    letter-spacing: 1px;
    color: var(--card-white);
  }
  .brand__tagline {
    margin-top: 10px;
    font-weight: 300;
    font-size: 22px;
    letter-spacing: 2px;
    color: var(--card-white);
  }
</style>
</head>
<body>

  <section class="card card--contact" aria-label="Business card contact side">
    <div class="details">
      <h1 class="details__name">Nora Vint</h1>
      <p class="details__title">Principal Makeup Artist</p>
      <div class="details__divider"></div>
      <ul class="contact">
        <li class="contact__item">
          <svg class="contact__icon" viewBox="0 0 14 14" aria-hidden="true">
            <rect width="14" height="14" fill="var(--accent-pink)"/>
            <path d="M4 3 L6 3 L6.6 5 L5.6 5.8 Q6.6 7.6 8.2 8.4 L9 7.4 L11 8 L11 10 Q6 10.6 4 3Z" fill="#fff"/>
          </svg>
          <span>0413 925 214</span>
        </li>
        <li class="contact__item">
          <svg class="contact__icon" viewBox="0 0 14 14" aria-hidden="true">
            <rect width="14" height="14" fill="var(--accent-pink)"/>
            <rect x="3" y="4" width="8" height="6" fill="none" stroke="#fff" stroke-width="1"/>
            <path d="M3 4 L7 7.4 L11 4" fill="none" stroke="#fff" stroke-width="1"/>
          </svg>
          <span>nora@lumirabeauty.com.au</span>
        </li>
        <li class="contact__item">
          <svg class="contact__icon" viewBox="0 0 14 14" aria-hidden="true">
            <rect width="14" height="14" fill="var(--accent-pink)"/>
            <circle cx="7" cy="7" r="4" fill="none" stroke="#fff" stroke-width="1"/>
            <ellipse cx="7" cy="7" rx="1.7" ry="4" fill="none" stroke="#fff" stroke-width="0.8"/>
            <path d="M3 7 H11" stroke="#fff" stroke-width="0.8"/>
          </svg>
          <span>www.lumirabeauty.com.au</span>
        </li>
      </ul>
    </div>
    <div class="card__rule"></div>
    <div class="card__band"></div>
  </section>

  <section class="card card--brand" aria-label="Business card brand side">
    <div class="brand">
      <p class="brand__name">Lumira</p>
      <p class="brand__tagline">MAKEUP ARTISTRY</p>
    </div>
    <div class="card__rule"></div>
    <div class="card__band"></div>
  </section>

</body>
</html>
```